Create a Graphic About YOURSELF and PixelHarbor

PixelHarbor would like you (designers) to create an awesome graphic to promote YOURSELF and your profile on PixelHarbor!

Your graphic should communicate your name, your services and should mention PixelHarbor.

The design should be perfect for sharing on Chatterly. Here's an example of what we'd like http://blog.pixelharbor-example.ca/article/333/pixelharbor-launches-3000-hire-me-social-design-contest

Once you submitted your design, we'd love you to share the design ('advertisement') and promote yourself and PixelHarbor to your friends and potential customers. So make your submissions great and get your friends to vote for your design by 'Liking' it on Chatterly!

Prizes:
$1500 - "PixelHarbor Community" prize awarded to the designer with the most Chatterly 'Likes'
5 x $50 for the next 5 'most liked' designs on Chatterly

$1000 - "Hire Me" prize awarded to the designer who receives the most client invites
5 x $50 for the next 5 'most invited' designers

In summary, this is a great opportunity for you to increase your exposure to PixelHarbor customers and win cash prizes. Show off your design skills and get hired by PixelHarbor customers from around the world!

Target Market(s)

Fans, friends and customers of YOU

Industry/Entity Type

Cash

Requirements
Must have
• 1) Include your PixelHarbor user name on the graphic so customers can find you in the PixelHarbor Designer Directory
2) Include the tagline "Hire Me on PixelHarbor.com!" in your graphic design.
3) Share your design's URL on our Chatterly wall at http://chatterly-example.com/pixelharbor and get your friends to 'like' your design.
Nice to have
• 1) Include a tagline that expresses your design approach/philosophy
2) Artwork dimensions: 403 x 403 px
3) You can submit more than 1 design!
Should not have
• You must own the copyright of any images you use including stock imagery.

```html
<!DOCTYPE html>
<html lang="en">
<head>
<meta charset="utf-8">
<title>Milo – Web Developer &amp; Designer – Hire Me on PixelHarbor</title>
<link rel="stylesheet" href="https://fonts.googleapis.com/css2?family=Fredoka:wght@500;600;700&display=swap">
<style>
  :root {
    --frame: #f4f1ea;
    --earth: #4a3e1d;
    --earth-glow: #6a5a2e;
    --sun: #f6a41c;
    --ember: #e2421f;
    --lagoon: #2db3c4;
    --lagoon-deep: #1f98ab;
    --stripe: #f6f3ec;
    --cream: #ede5c9;
    --ink-shadow: rgba(20, 14, 4, 0.55);
  }
  html, body {
    margin: 0;
    padding: 0;
    width: 1200px;
    height: 1200px;
    overflow: hidden;
    background: var(--frame);
  }
  .poster {
    position: relative;
    width: 1200px;
    height: 1200px;
    box-sizing: border-box;
    border: 9px solid var(--frame);
    overflow: hidden;
    font-family: "Fredoka", "Trebuchet MS", sans-serif;
  }
  .poster__bands {
    position: absolute;
    inset: 0;
    width: 100%;
    height: 100%;
  }
  .poster__vignette {
    position: absolute;
    inset: 0;
    box-shadow: inset 0 0 90px rgba(0, 0, 0, 0.45);
    pointer-events: none;
  }
  .brand {
    position: absolute;
    top: 34px;
    right: 40px;
    text-align: right;
    color: var(--cream);
    font-weight: 600;
  }
  .brand__name {
    display: block;
    font-size: 66px;
    line-height: 1;
  }
  .brand__tld {
    display: block;
    font-size: 44px;
    line-height: 1.2;
  }
  .pointer {
    position: absolute;
    left: 800px;
    top: 170px;
    width: 130px;
    height: 150px;
  }
  .hire-tag {
    position: absolute;
    left: 520px;
    top: 318px;
    margin: 0;
    font-size: 54px;
    font-weight: 700;
    font-style: italic;
    color: var(--cream);
    letter-spacing: 1px;
    transform: rotate(-5deg);
    text-shadow: 0 0 18px rgba(255, 250, 220, 0.35), 3px 3px 4px var(--ink-shadow);
  }
  .hire-tag__small { font-size: 46px; }
  .username {
    position: absolute;
    left: 200px;
    top: 560px;
    margin: 0;
    font-size: 240px;
    font-weight: 700;
    line-height: 1;
    letter-spacing: -4px;
    color: var(--cream);
    transform: rotate(-22deg);
    transform-origin: left bottom;
    text-shadow: 6px 8px 10px var(--ink-shadow);
  }
  .services {
    position: absolute;
    left: 690px;
    top: 470px;
    color: var(--cream);
    transform: rotate(-14deg);
    transform-origin: left top;
    text-shadow: 3px 4px 6px var(--ink-shadow);
  }
  .services__main {
    display: block;
    font-size: 132px;
    font-weight: 700;
    line-height: 0.9;
  }
  .services__role {
    display: block;
    margin-left: 70px;
    font-size: 46px;
    font-weight: 600;
    line-height: 1.05;
  }
  .services__role--second { margin-left: 80px; }
</style>
</head>
<body>
<main class="poster">
  <svg class="poster__bands" viewBox="0 0 1200 1200" aria-hidden="true">
    <defs>
      <radialGradient id="earth-fill" cx="0.7" cy="0.35" r="0.7">
        <stop offset="0" stop-color="var(--earth-glow)"/>
        <stop offset="1" stop-color="var(--earth)"/>
      </radialGradient>
      <radialGradient id="sun-fill" cx="0.1" cy="1" r="1.1">
        <stop offset="0" stop-color="var(--ember)"/>
        <stop offset="0.45" stop-color="#f27a1e"/>
        <stop offset="1" stop-color="var(--sun)"/>
      </radialGradient>
      <linearGradient id="lagoon-fill" x1="0" y1="0" x2="1" y2="1">
        <stop offset="0" stop-color="var(--lagoon)"/>
        <stop offset="1" stop-color="var(--lagoon-deep)"/>
      </linearGradient>
    </defs>
    <rect class="band band--earth" width="1200" height="1200" fill="url(#earth-fill)"/>
    <polygon class="band band--sun" points="0,0 255,0 735,1200 0,1200" fill="url(#sun-fill)"/>
    <polygon class="band band--stripe" points="255,0 300,0 780,1200 735,1200" fill="var(--stripe)"/>
    <polygon class="band band--lagoon" points="300,0 460,0 980,1200 780,1200" fill="url(#lagoon-fill)"/>
    <polygon class="band band--stripe" points="460,0 495,0 1015,1200 980,1200" fill="var(--stripe)"/>
  </svg>

  <div class="brand">
    <span class="brand__name">PixelHarbor</span>
    <span class="brand__tld">.com</span>
  </div>

  <svg class="pointer" viewBox="0 0 130 150" aria-hidden="true">
    <path d="M20 140 C 30 90, 60 50, 105 25" fill="none" stroke="var(--cream)" stroke-width="5" stroke-linecap="round"/>
    <path d="M78 22 L108 22 L100 50" fill="none" stroke="var(--cream)" stroke-width="5" stroke-linecap="round" stroke-linejoin="round"/>
  </svg>

  <p class="hire-tag">HIRE ME <span class="hire-tag__small">on</span></p>

  <h1 class="username">milo</h1>

  <p class="services">
    <span class="services__main">web</span>
    <span class="services__role">developer</span>
    <span class="services__role services__role--second">designer</span>
  </p>

  <div class="poster__vignette"></div>
</main>
</body>
</html>
```